New Website Deisgn. Guaranteed Project.

I would like a site similar to this: http://givewheelsheal.org.

old site: http://autosforrelief.org

Create a professional website; a car donation site seeking leads to return calls.

Please see http://givewheelsheal.org for the concept I am after.

The webpage should have a professional feel. The pages to include are 'Home', 'About us' and 'Get Started'

Industry/Entity Type

It Professional

Coding

Coded - Design and coding required

Number of Pages Required

1 page

```html
<!DOCTYPE html>
<html lang="en">
<head>
<meta charset="utf-8">
<title>Bright Futures Kids Relief – Donate Your Car</title>
<link rel="stylesheet" href="https://fonts.googleapis.com/css2?family=Open+Sans:wght@400;600;700&family=Arimo:wght@400;700&display=swap">
<style>
:root{
  --ink:#222;
  --black:#000;
  --footer:#1b1b1b;
  --purple:#3b3684;
  --purple-dark:#37327a;
  --red:#d9342b;
  --yellow:#f8d20a;
  --green:#8da23b;
  --pink:#e0666e;
  --grey-bg:#f3f3f3;
}
*{box-sizing:border-box;margin:0;padding:0}
html,body{width:1200px;height:3020px;overflow:hidden}
body{position:relative;background:#fff;font-family:"Open Sans",Arial,sans-serif;color:var(--ink)}
.abs{position:absolute}

/* header */
.brand{left:100px;top:18px;display:flex;align-items:center;gap:12px}
.brand-mark{width:70px;height:70px;border-radius:6px;background:var(--purple)}
.brand-name{width:170px;font-size:18px;line-height:20px;color:var(--purple)}
.social-top{left:728px;top:46px;display:flex;gap:9px}
.dot{width:28px;height:28px;border-radius:50%;background:var(--purple)}
.call{left:888px;top:44px;display:flex;align-items:center;gap:10px;font-size:17px}
.call b{font-size:20px;font-weight:600;margin-left:6px}

.nav{left:0;top:115px;width:1200px;height:57px;background:var(--black);display:flex;align-items:center;padding-left:102px}
.nav a{color:#fff;text-decoration:none;font-size:14px;font-weight:700;font-family:Arimo,Arial,sans-serif}
.nav .sep{color:#fff;margin:0 26px;font-size:14px}

/* hero */
.hero{left:0;top:172px;width:1200px;height:482px;background:linear-gradient(90deg,#cfcfcf,#e8e8e8 60%,#dedede)}
.hero-photo{left:0;top:172px;width:600px;height:482px;background:linear-gradient(135deg,#8f7f9a,#b79a86 45%,#7a7474)}
.hero-rule{left:0;top:654px;width:1200px;height:8px;background:var(--purple)}
.headline{left:622px;top:222px;font-family:Arimo,Arial,sans-serif;font-weight:700;font-size:40px;line-height:41px;color:#111}
.headline .d{color:var(--purple)}
.headline .y{color:var(--red)}
.headline .c{color:#e3b600}
.headline .t{color:#5aa33a}
.hero-cars{left:472px;top:480px;width:362px;height:170px;background:linear-gradient(180deg,#e4e4e4,#c4c4c4)}

.signup{left:842px;top:180px;width:260px;height:450px;background:var(--yellow);border-radius:4px}
.signup-head{left:842px;top:180px;width:260px;height:68px;background:var(--black);border-radius:4px 4px 0 0;color:var(--yellow);font-size:34px;text-align:center;line-height:66px}
.signup-notch{left:956px;top:247px}
.field{position:absolute;height:32px;background:#fff;border:1px solid #d9c36a;font-size:13px;color:#888;padding:7px 8px;font-family:Arimo,Arial,sans-serif;display:flex;justify-content:space-between;align-items:center}
.field.full{left:860px;width:222px}
.field.half{width:108px}
.btn-donate{left:892px;top:556px;width:162px;height:46px;background:var(--black);color:var(--yellow);font-weight:700;font-size:18px;text-align:center;line-height:46px;font-family:Arimo,Arial,sans-serif;border-radius:3px}

/* how it works */
.how{left:0;top:662px;width:1200px;height:466px;background:linear-gradient(180deg,#fff,#eeeeee)}
.section-title{width:1200px;left:0;text-align:center;font-weight:700;font-size:31px;color:var(--purple)}
.intro{left:270px;width:660px;top:776px;text-align:center;font-size:14px;line-height:24px;color:#333;font-family:Arimo,Arial,sans-serif}
.step{position:absolute;top:868px;display:flex;align-items:center;gap:16px}
.step-ring{width:156px;height:156px;border-radius:50%;background:#e4e4e4;display:flex;align-items:center;justify-content:center;box-shadow:inset 0 0 0 10px #ececec}
.step-core{width:114px;height:114px;border-radius:50%;background:#fff;display:flex;align-items:center;justify-content:center}
.step-text small{display:block;font-size:12px;font-style:italic;color:#333;font-family:Arimo,Arial,sans-serif}
.step-text h3{font-size:27px;line-height:27px;color:#2a2a2a;font-weight:600;margin:4px 0;letter-spacing:-.5px}
.step-text a{font-size:12px;font-style:italic;color:var(--purple);text-decoration:none;font-family:Arimo,Arial,sans-serif}

/* feature cards */
.card{position:absolute;top:1214px;width:226px;height:328px;border-radius:14px;text-align:center;color:#fff;padding:14px 14px 0}
.card-photo{height:122px;border-radius:12px;border:3px solid #fff}
.card h4{margin-top:14px;font-size:18px;line-height:21px;font-weight:400}
.card p{font-size:12px;line-height:15px;margin:6px 10px 0;font-family:Arimo,Arial,sans-serif}
.card .more{position:absolute;left:16px;right:16px;bottom:28px;height:36px;line-height:36px;font-size:14px;font-family:Arimo,Arial,sans-serif}
.c-green{left:103px;background:var(--green)} .c-green .more{background:#a0b45a}
.c-pink{left:362px;background:var(--pink)} .c-pink .more{background:#ec8488}
.c-purple{left:616px;background:var(--purple)} .c-purple .more{background:#5851a0}
.c-yellow{left:876px;background:var(--yellow)} .c-yellow .more{background:#fbe040}

/* about */
.about{left:0;top:1630px;width:1200px;height:450px;background:var(--grey-bg)}
.about-title{left:100px;top:1660px;font-weight:400;font-size:30px;color:#222}
.about-sub{left:100px;top:1706px;font-size:16px;font-weight:600}
.about-copy{left:100px;top:1738px;width:600px;font-size:15.5px;line-height:26px;color:#444}
.about-copy p+p{margin-top:26px}
.about-art{left:700px;top:1720px;width:500px;height:360px;background:linear-gradient(180deg,#f6e7d6,#f3b36c)}

/* services */
.services-photo{left:0;top:2080px;width:525px;height:420px;background:linear-gradient(135deg,#caa98a,#a07e67 50%,#e6d8c8)}
.services{left:525px;top:2080px;width:675px;height:420px;background:var(--purple-dark);color:#fff;padding:42px 0 0 50px}
.services h2{font-weight:400;font-size:28px;margin-bottom:20px}
.services li{list-style:none;display:flex;align-items:center;gap:14px;font-size:16px;height:37.5px;color:#e8e8f4}
.btn-outline{display:inline-block;margin-top:22px;border:1.5px solid #fff;border-radius:6px;padding:7px 22px;font-size:14px}

/* testimonial */
.testi-title{left:0;width:1200px;top:2576px;text-align:center;font-size:32px;color:#333;font-weight:400}
.quote{position:absolute;top:2672px;display:flex;gap:22px}
.avatar{width:100px;height:100px;border-radius:50%;background:#cbbba8;border:4px solid #eee;flex:none}
.quote-body{width:360px;font-family:Arimo,Arial,sans-serif}
.quote-mark{color:var(--purple);font-size:26px;font-weight:700;line-height:22px}
.quote-body b{font-size:14px}
.quote-body p{font-size:12.5px;line-height:17px;color:#333;margin-top:4px}
.quote-body cite{display:block;margin-top:12px;font-size:13px;color:var(--purple);font-style:normal}

/* footer */
.footer{left:0;top:2870px;width:1200px;height:150px;background:var(--footer);color:#ddd;font-family:Arimo,Arial,sans-serif}
.footer-links{position:absolute;top:28px;width:1200px;text-align:center;font-size:13px}
.footer-links .sep{margin:0 12px}
.footer-social{position:absolute;top:60px;width:1200px;display:flex;justify-content:center;gap:10px}
.footer-social .dot{width:30px;height:30px;background:#555;border:2px solid #fff}
.copyright{position:absolute;top:112px;width:1200px;text-align:center;font-size:12px;color:#aaa}
</style>
</head>
<body>

<div class="abs brand"><span class="brand-mark"></span><span class="brand-name">Bright Futures Kids Relief</span></div>
<div class="abs social-top"><span class="dot"></span><span class="dot"></span><span class="dot"></span><span class="dot"></span></div>
<div class="abs call">
  <svg width="16" height="26" viewBox="0 0 16 26"><rect x="1" y="1" width="14" height="24" rx="3" fill="none" stroke="#3b3684" stroke-width="2"/><circle cx="8" cy="21" r="1.5" fill="#3b3684"/></svg>
  <span>Call Us: <b>555 014 2290</b></span>
</div>
<nav class="abs nav"><a>HOME</a><span class="sep">|</span><a>ABOUT US</a><span class="sep">|</span><a>GALLERY</a><span class="sep">|</span><a>CONTACT US</a></nav>

<div class="abs hero"></div>
<div class="abs hero-photo" role="img" aria-label="Smiling child in a purple head scarf holding a soft toy"></div>
<div class="abs headline">
  <div><span class="d">D</span>ONATE</div>
  <div><span class="y">Y</span>OUR</div>
  <div><span class="c">C</span>AR</div>
  <div><span class="t">T</span>O FIGHT</div>
  <div><span class="d">C</span>HILDREN</div>
  <div><span class="y">C</span>ANCER</div>
</div>
<div class="abs hero-cars" role="img" aria-label="Two silver sedans parked side by side"></div>
<div class="abs hero-rule"></div>

<div class="abs signup"></div>
<div class="abs signup-head">Sign Up</div>
<svg class="abs signup-notch" width="34" height="18" viewBox="0 0 34 18"><path d="M0 0H34L17 18Z" fill="#000"/></svg>
<div class="field full" style="top:288px">First name</div>
<div class="field full" style="top:338px">Phone number</div>
<div class="field full" style="top:388px">Country</div>
<div class="field half" style="left:860px;top:440px">Choose year <span>▾</span></div>
<div class="field half" style="left:974px;top:440px">Choose make <span>▾</span></div>
<div class="field half" style="left:860px;top:490px">Model <span>▾</span></div>
<div class="field half" style="left:974px;top:490px">Zip code <span>▾</span></div>
<div class="abs btn-donate">DONATE</div>

<div class="abs how"></div>
<h2 class="abs section-title" style="top:720px">HOW IT WORKS ?</h2>
<p class="abs intro">Lorem ipsum dolor sit amet, consectetur adipiscing elit, sed do eiusmod tempor incididunt ut labore et dolore magna aliqua.</p>

<div class="step" style="left:100px">
  <div class="step-ring"><div class="step-core">
    <svg width="58" height="64" viewBox="0 0 58 64"><rect x="4" y="2" width="42" height="56" rx="3" fill="none" stroke="#2e2a6e" stroke-width="4"/><path d="M13 16h24M13 26h24M13 36h16" stroke="#2e2a6e" stroke-width="4"/><rect x="32" y="38" width="22" height="22" fill="#fff" stroke="#2e2a6e" stroke-width="3"/><path d="M37 49l4 4 8-9" fill="none" stroke="#2e2a6e" stroke-width="3"/></svg>
  </div></div>
  <div class="step-text"><small>lorem ipsum dolor</small><h3>FILL FORM</h3><a>learn more ››</a></div>
</div>
<div class="step" style="left:420px">
  <div class="step-ring"><div class="step-core">
    <svg width="80" height="44" viewBox="0 0 80 44"><path d="M2 30h44V16h14l10 10 8 4v4H2z" fill="#2e2a6e"/><path d="M10 6l22 16" stroke="#2e2a6e" stroke-width="4"/><rect x="52" y="19" width="8" height="7" fill="#fff"/><circle cx="16" cy="36" r="6" fill="#2e2a6e" stroke="#fff" stroke-width="2"/><circle cx="62" cy="36" r="6" fill="#2e2a6e" stroke="#fff" stroke-width="2"/></svg>
  </div></div>
  <div class="step-text"><small>lorem ipsum dolor</small><h3>SCHEDULE<br>PICK UP</h3><a>learn more ››</a></div>
</div>
<div class="step" style="left:760px">
  <div class="step-ring"><div class="step-core">
    <svg width="56" height="64" viewBox="0 0 56 64"><path d="M4 2h36l12 12v48H4z" fill="#2e2a6e"/><path d="M12 16h20M12 26h32M12 36h14M12 46h14" stroke="#fff" stroke-width="4"/><text x="34" y="52" font-size="20" font-family="Arial" font-weight="700" fill="#fff">$</text></svg>
  </div></div>
  <div class="step-text"><small>lorem ipsum dolor</small><h3>RECIEVE TAX<br>DEDUCTION</h3><a>learn more ››</a></div>
</div>

<div class="card c-green">
  <div class="card-photo" role="img" aria-label="Car keys being handed over" style="background:linear-gradient(135deg,#d8cdbf,#8d8578)"></div>
  <h4>WE ACCEPT ALL CARS</h4>
  <p>simply dummy text of the printing and typesetting industry. Lorem Ipsum has been the industry</p>
  <div class="more">Readmore</div>
</div>
<div class="card c-pink">
  <div class="card-photo" role="img" aria-label="Stacked hands of volunteers" style="background:linear-gradient(135deg,#a87a5e,#4e3a30)"></div>
  <h4>CHARITY PROGRAMS</h4>
  <p>simply dummy text of the printing and typesetting industry. Lorem Ipsum has been the industry</p>
  <div class="more">Readmore</div>
</div>
<div class="card c-purple">
  <div class="card-photo" role="img" aria-label="Hands holding a young green plant" style="background:linear-gradient(135deg,#eef2d8,#8cb04a)"></div>
  <h4>HASSLE FREE DONATIONS</h4>
  <p>simply dummy text of the printing and typesetting industry. Lorem Ipsum has been the industry</p>
  <div class="more">Readmore</div>
</div>
<div class="card c-yellow">
  <div class="card-photo" role="img" aria-label="Crowd at a car auction" style="background:linear-gradient(135deg,#b8b0aa,#7c6c6c)"></div>
  <h4>SOLD ON lARGEST AUCTION NETWORK</h4>
  <p>simply dummy text of the printing and typesetting industry. Lorem Ipsum has been the industry</p>
  <div class="more">Readmore</div>
</div>

<div class="abs about"></div>
<h2 class="abs about-title">ABOUT US</h2>
<div class="abs about-sub">nullam males ua da erat ut turp is</div>
<div class="abs about-copy">
  <p>Vivamus vestibulum neque quis nunc convallis venenatis. Nulla tristique lorem sit amet ipsum ornare sit amet feugiat nulla condimentum. Sed faucibus volutpat nunc, at ullamcorper augue elementum id. Quisque at lectus leo, nec placerat mi.</p>
  <p>Vivamus vestibulum neque quis nunc convallis venenatis. Nulla tristique lorem sit amet ipsum ornare sit amet feugiat nulla condimentum. Sed faucibus volutpat nunc, at ullamcorper augu. Donec iaculis tempor tempor. Mauris ut mauris eget orci mattis scelerisque eu in risus. Maecenas consectetur risus at libero commodo suscipit.Donec iaculis tempor tempor. Mauris ut mauris eget</p>
</div>
<div class="abs about-art" role="img" aria-label="Illustration of many raised colourful hands, one holding a heart"></div>

<div class="abs services-photo" role="img" aria-label="Mother comforting her child"></div>
<section class="abs services">
  <h2>OUR SERVICES</h2>
  <ul>
    <li><svg width="20" height="20" viewBox="0 0 20 20"><rect x="1" y="1" width="18" height="18" rx="3" fill="none" stroke="#fff" stroke-width="2"/><path d="M5 10l4 4 7-8" fill="none" stroke="#fff" stroke-width="2"/></svg>Car donations are easy</li>
    <li><svg width="20" height="20" viewBox="0 0 20 20"><rect x="1" y="1" width="18" height="18" rx="3" fill="none" stroke="#fff" stroke-width="2"/><path d="M5 10l4 4 7-8" fill="none" stroke="#fff" stroke-width="2"/></svg>Free Pick up National wide</li>
    <li><svg width="20" height="20" viewBox="0 0 20 20"><rect x="1" y="1" width="18" height="18" rx="3" fill="none" stroke="#fff" stroke-width="2"/><path d="M5 10l4 4 7-8" fill="none" stroke="#fff" stroke-width="2"/></svg>Tax Deductible</li>
    <li><svg width="20" height="20" viewBox="0 0 20 20"><rect x="1" y="1" width="18" height="18" rx="3" fill="none" stroke="#fff" stroke-width="2"/><path d="M5 10l4 4 7-8" fill="none" stroke="#fff" stroke-width="2"/></svg>No Paperwork Hassle</li>
    <li><svg width="20" height="20" viewBox="0 0 20 20"><rect x="1" y="1" width="18" height="18" rx="3" fill="none" stroke="#fff" stroke-width="2"/><path d="M5 10l4 4 7-8" fill="none" stroke="#fff" stroke-width="2"/></svg>Avoid the hassle of trying to sell Used Car</li>
    <li><svg width="20" height="20" viewBox="0 0 20 20"><rect x="1" y="1" width="18" height="18" rx="3" fill="none" stroke="#fff" stroke-width="2"/><path d="M5 10l4 4 7-8" fill="none" stroke="#fff" stroke-width="2"/></svg>Save money on car bills</li>
  </ul>
  <span class="btn-outline">Read more</span>
</section>

<h2 class="abs testi-title">TESTIMONIAL</h2>
<div class="quote" style="left:120px">
  <div class="avatar" role="img" aria-label="Portrait of a woman"></div>
  <div class="quote-body">
    <div class="quote-mark">“</div>
    <b>Lorem ipsum dolor sit amet,</b>
    <p>consectetur adipisicing elit, sed do eiusmod tempor incididunt ut labore et dolore magna aliqua. Ut enim ad minim veniam, quis nostrud exercitation ullamco laboris nisi ut aliquip</p>
    <cite>- Ms. Clara Wynn</cite>
  </div>
</div>
<div class="quote" style="left:628px">
  <div class="avatar" role="img" aria-label="Portrait of a man in a suit" style="width:92px;height:92px;background:#9b8878"></div>
  <div class="quote-body">
    <div class="quote-mark">“</div>
    <b>Lorem ipsum dolor sit amet,</b>
    <p>consectetur adipisicing elit, sed do eiusmod tempor incididunt ut labore et dolore magna aliqua. Ut enim ad minim veniam, quis nostrud exercitation ullamco laboris nisi ut aliquip</p>
    <cite>- Mr. Daniel Hart</cite>
  </div>
</div>

<footer class="abs footer">
  <div class="footer-links">Vendors<span class="sep">|</span>Protection Types<span class="sep">|</span>Products<span class="sep">|</span>Market Analysis<span class="sep">|</span>Subscribe</div>
  <div class="footer-social"><span class="dot"></span><span class="dot"></span><span class="dot"></span><span class="dot"></span><span class="dot"></span><span class="dot"></span></div>
  <div class="copyright">Copyright© 2015 &nbsp;digital &amp; social media marketing. &nbsp;All rights reserved.</div>
</footer>

</body>
</html>
```